business card design for a small scale specialty cut flower farm

We need a business card design for Hollowmere Bloom Farm based in Langley, BC, Canada. We produce specialty, high-end cut flowers and sell locally to florists, local shops and markets and the end user through bouquet subscriptions. The final business card design should be memorable and have a timeless or vintage feel. We would prefer a square shape.
Updates

Target Market(s)

florists, shops and seasonal markets, local flower lovers

Industry/Entity Type

Floral

Contact Information for Business Card

Tamsin Ellery Voss, Grower
Langley, BC, Canada
website: hollowmerebloomfarm.example
instagram: @hollowmerebloomfarm
Tel: 555.317.4290
facebook: www.facebook.example/hollowmereblooms/

Font styles to use
Serif
Decorative
Script

Requirements
Must have
• soft black background colour on front side, the included logo and catch phrase: Fresh Local Seasonal
Nice to have
• phone number and website address on front of card, included photo 6539 incorporated onto the back, possibly photo 6609 as well.

```html
<!DOCTYPE html>
<html lang="en">
<head>
<meta charset="utf-8">
<title>Hollowmere Bloom Farm – Business Card</title>
<link href="https://fonts.googleapis.com/css2?family=Mulish:wght@300;400;500&display=swap" rel="stylesheet">
<style>
  :root {
    --backdrop: #8e8e8e;
    --card-light: #ffffff;
    --card-dark: #231f20;
    --ink: #1b1b1b;
    --ink-soft: #7a7a7a;
    --divider: #9a9a9a;
    --paper-text: #ffffff;
  }
  * { margin: 0; padding: 0; box-sizing: border-box; }
  html, body {
    width: 1200px; height: 960px; overflow: hidden;
    background: var(--backdrop);
    font-family: "Mulish", Arial, sans-serif;
  }
  .card {
    position: absolute; left: 281px;
    width: 655px; height: 374px;
    border-radius: 26px;
  }
  .card--front { top: 59px; background: var(--card-light); }
  .card--back { top: 501px; background: var(--card-dark); }

  /* front */
  .brand-mark {
    position: absolute; left: 98px; top: 150px; width: 225px;
    text-align: center; color: var(--ink);
    font-weight: 400; font-size: 17px; letter-spacing: 0.22em;
    line-height: 1.5; text-transform: uppercase;
  }
  .divider {
    position: absolute; left: 328px; top: 107px;
    width: 1.5px; height: 161px; background: var(--divider);
  }
  .person { position: absolute; left: 349px; top: 103px; }
  .person__name { font-size: 24px; font-weight: 500; color: var(--ink); line-height: 1.2; }
  .person__role { font-size: 17px; font-weight: 300; color: var(--ink-soft); line-height: 1.3; }
  .contact-list {
    position: absolute; left: 349px; top: 175px; list-style: none;
  }
  .contact-list li {
    display: flex; align-items: center; gap: 8px;
    height: 23.5px; font-size: 16px; font-weight: 300; color: var(--ink-soft);
  }
  .contact-list svg { width: 18px; height: 18px; flex: none; }

  /* back */
  .brand-mark--back {
    position: absolute; left: 0; right: 0; top: 175px;
    text-align: center; color: var(--paper-text);
    font-size: 24px; font-weight: 400; letter-spacing: 0.24em;
    text-transform: uppercase;
  }
  .tagline {
    position: absolute; left: 130px; right: 130px; top: 304px;
    display: flex; align-items: center; gap: 8px;
    color: var(--paper-text); font-size: 17px; font-weight: 400;
  }
  .tagline::before, .tagline::after {
    content: ""; flex: 1; height: 1.5px; background: var(--paper-text);
  }
  .tagline::before { background: linear-gradient(to right, transparent, var(--paper-text)); }
  .tagline::after { background: linear-gradient(to left, transparent, var(--paper-text)); }
</style>
</head>
<body>
  <section class="card card--front">
    <div class="brand-mark">Hollowmere<br>Bloom Farm</div>
    <div class="divider"></div>
    <div class="person">
      <p class="person__name">Tamsin Ellery Voss</p>
      <p class="person__role">Owner</p>
    </div>
    <ul class="contact-list">
      <li>
        <svg viewBox="0 0 18 18" aria-hidden="true"><circle cx="9" cy="9" r="9" fill="#1b1b1b"/><path d="M6.2 4.6l1.6 2.2-.9 1c.6 1.2 1.4 2 2.6 2.6l1-.9 2.2 1.6-.8 1.6c-3.4-.3-6.4-3.3-6.7-6.7z" fill="#fff"/></svg>
        (555) 317-4290
      </li>
      <li>
        <svg viewBox="0 0 18 18" aria-hidden="true"><circle cx="9" cy="9" r="9" fill="#1b1b1b"/><g fill="none" stroke="#fff" stroke-width="1"><circle cx="9" cy="9" r="5"/><ellipse cx="9" cy="9" rx="2.2" ry="5"/><path d="M4 9h10M5 6.5h8M5 11.5h8"/></g></svg>
        hollowmerebloomfarm.example
      </li>
      <li>
        <svg viewBox="0 0 18 18" aria-hidden="true"><circle cx="9" cy="9" r="9" fill="#1b1b1b"/></svg>
        @hollowmerebloomfarm
      </li>
      <li>
        <svg viewBox="0 0 18 18" aria-hidden="true"><circle cx="9" cy="9" r="9" fill="#1b1b1b"/></svg>
        hollowmereblooms
      </li>
    </ul>
  </section>

  <section class="card card--back">
    <div class="brand-mark--back">Hollowmere Bloom Farm</div>
    <p class="tagline">Fresh Local Seasonal</p>
  </section>
</body>
</html>
```